Wine label design for my wife. Wine called "The Mirabel"

I need a wine label face lift of one of my premium wines in my collection. My wine sells in Harbor Lark's all over the States. My current label is called The Mirabel (my wife's name) and the illustration of her eyes is done by a well know artist from South Africa. I do not have to use this illustration and therefor I attached several pictures of her and her eyes, even when she was a little girl. The wine's also made in South Africa. This is a premium wine that we only sell 2000 bottles per year. The wine sells at 60 usd per bottle, The current label is too white. I also think her eyes should look more at the person buying it, than away from them.

Target Market(s)

Top end wine buyers

Font styles to use
Decorative
Script

Requirements
Must have
• 'The Mirabel' must be on the label
An illustration must be on the label
Basically all the info that's on the current label must be on by law. As per Sample
Nice to have
• Maybe some ideas of her whole face?
Should not have
• any gold colour

```html
<!DOCTYPE html>
<html lang="en">
<head>
<meta charset="utf-8">
<title>The Mirabel – Sauvignon Blanc Label</title>
<link rel="stylesheet" href="https://fonts.googleapis.com/css2?family=Pinyon+Script&family=Marcellus+SC&family=Alegreya:ital@1&display=swap">
<style>
  :root {
    --page: #ffffff;
    --label-ink: #18191b;
    --label-edge: #c9c9c9;
    --text-light: #ffffff;
    --text-muted: #a6a7a9;
    --portrait-light: #f4f4f2;
    --portrait-mid: #cfcfcc;
    --portrait-dark: #4a4a48;
  }
  * { box-sizing: border-box; margin: 0; padding: 0; }
  html, body {
    width: 1200px;
    height: 743px;
    overflow: hidden;
    background: var(--page);
  }
  .canvas {
    position: relative;
    width: 1200px;
    height: 743px;
    display: flex;
    align-items: center;
    justify-content: center;
  }
  .wine-label {
    position: relative;
    width: 498px;
    height: 663px;
    background: var(--label-ink);
    outline: 1px solid var(--label-edge);
    color: var(--text-light);
  }
  .label-title {
    position: absolute;
    top: 0;
    left: 0;
    width: 100%;
    height: 203px;
    display: flex;
    align-items: center;
    justify-content: center;
    padding-top: 8px;
    font-family: "Pinyon Script", cursive;
    font-weight: 400;
    font-size: 70px;
    line-height: 1;
    white-space: nowrap;
  }
  .label-portrait {
    position: absolute;
    top: 203px;
    left: 0;
    width: 100%;
    height: 166px;
    background:
      radial-gradient(ellipse 60% 70% at 50% 55%, var(--portrait-light) 0%, var(--portrait-light) 45%, var(--portrait-mid) 80%, transparent 100%),
      linear-gradient(90deg, var(--portrait-dark) 0%, var(--portrait-mid) 14%, var(--portrait-light) 30%, var(--portrait-light) 70%, var(--portrait-mid) 86%, var(--portrait-dark) 100%);
  }
  .label-details {
    position: absolute;
    left: 0;
    width: 100%;
    text-align: center;
  }
  .vintage {
    top: 394px;
    font-family: "Alegreya", serif;
    font-style: italic;
    font-size: 22px;
    letter-spacing: 0.5px;
  }
  .varietal {
    top: 432px;
    font-family: "Marcellus SC", serif;
    font-size: 26px;
    letter-spacing: 2.5px;
  }
  .divider {
    position: absolute;
    top: 510px;
    left: 222px;
    width: 55px;
    height: 4px;
    background: var(--text-light);
  }
  .producer {
    top: 566px;
    font-family: "Marcellus SC", serif;
    font-size: 40px;
    letter-spacing: 2px;
    color: var(--text-muted);
    white-space: nowrap;
  }
</style>
</head>
<body>
  <main class="canvas">
    <article class="wine-label">
      <h1 class="label-title">The Mirabel</h1>
      <div class="label-portrait" role="img" aria-label="Black and white illustration of a woman's eyes and brows"></div>
      <p class="label-details vintage">2017</p>
      <p class="label-details varietal">SAUVIGNON BLANC</p>
      <div class="divider"></div>
      <p class="label-details producer">Adrian Holt Wines</p>
    </article>
  </main>
</body>
</html>
```